Brightpath Holdings Business Card

Create a two sided, high gloss, quality business card for Brightpath Holdings.

Target Market(s)

People wanting to purchase, scale, and sell businesses.

Industry/Entity Type

Entrepreneurs

Contact Information for Business Card

One line: Dana Corwell, CPA, CMA Another line: Entrepreneur & Investor Another line: Business Ownership Transition Expert Another line: Multi-State Licensed Real Estate Broker Phone 954-BRTPATH (278-7284) Email Dana@Brightpath Holdings.com Website www.Brightpath.com

Requirements
Must have
• Black Card, logo on one side, all other information on the other side including a small logo.
Nice to have
• Possibly add a tagline "Helping entrepreneurs live a life they don't need a vacation from"
Should not have
• There will not be a mailing address on these cards.

```html
<!DOCTYPE html>
<html lang="en">
<head>
<meta charset="utf-8">
<title>Brightpath Holdings Business Card</title>
<link rel="stylesheet" href="https://fonts.googleapis.com/css2?family=Montserrat:wght@400;700&family=Open+Sans:wght@400;700&display=swap">
<style>
  :root {
    --stage: #1c1c1c;
    --card-black: #050505;
    --gold-deep: #c9a23a;
    --gold-mid: #e6c76a;
    --gold-light: #fbf3c4;
    --ink: #111111;
    --white: #ffffff;
  }
  * { box-sizing: border-box; margin: 0; padding: 0; }
  html, body { width: 1200px; height: 1015px; overflow: hidden; }
  body {
    background: var(--stage);
    display: flex; flex-direction: column; align-items: center; justify-content: center;
    gap: 44px;
    font-family: "Open Sans", sans-serif;
  }
  .card {
    position: relative;
    width: 760px; height: 434px;
    background: var(--card-black);
    overflow: hidden;
    box-shadow: 0 10px 30px rgba(0,0,0,.55);
  }
  /* Back side */
  .card-back { display: flex; flex-direction: column; align-items: center; justify-content: center; gap: 40px; }
  .brand-mark { display: flex; align-items: center; gap: 14px; }
  .brand-dot { width: 22px; height: 22px; border-radius: 50%; background: var(--gold-mid); }
  .brand-name {
    font-family: "Montserrat", sans-serif; font-weight: 700;
    color: var(--gold-mid); font-size: 48px; letter-spacing: .5px;
  }
  .tagline {
    font-family: "Montserrat", sans-serif; font-weight: 400;
    color: var(--white); font-size: 21px; line-height: 1.3; text-align: center;
  }
  /* Front side */
  .gold-band { position: absolute; inset: 0; }
  .portrait {
    position: absolute; right: 30px; top: 50px; width: 270px; height: 384px;
    background: linear-gradient(180deg, #6a4a2e 0%, #8b6442 30%, #e0b84a 55%, #1b1b24 75%);
    border-radius: 120px 120px 0 0;
    opacity: .9;
  }
  .front-logo { position: absolute; left: 44px; top: 70px; }
  .front-logo .brand-name { font-size: 34px; }
  .front-logo .brand-dot { width: 16px; height: 16px; }
  .details { position: absolute; left: 44px; top: 220px; color: var(--ink); }
  .person-name { font-size: 30px; font-weight: 700; line-height: 1.1; }
  .person-name .credentials { font-weight: 400; font-size: 24px; }
  .roles { list-style: none; font-size: 17px; line-height: 1.3; margin-top: 6px; }
  .contacts { list-style: none; font-size: 17px; line-height: 1.55; margin-top: 14px; }
  .contacts li { display: flex; align-items: center; gap: 12px; }
  .contacts svg { width: 18px; height: 18px; flex: none; }
</style>
</head>
<body>

<section class="card card-back" aria-label="Card back">
  <div class="brand-mark">
    <span class="brand-dot"></span>
    <span class="brand-name">Brightpath Holdings</span>
  </div>
  <p class="tagline">Helping entrepreneurs live a life they don't need<br>a vacation from</p>
</section>

<section class="card card-front" aria-label="Card front">
  <svg class="gold-band" viewBox="0 0 760 434" preserveAspectRatio="none" aria-hidden="true">
    <defs>
      <linearGradient id="goldFill" x1="0" y1="1" x2="1" y2="0">
        <stop offset="0" stop-color="var(--gold-deep)"/>
        <stop offset=".55" stop-color="var(--gold-light)"/>
        <stop offset="1" stop-color="var(--gold-mid)"/>
      </linearGradient>
    </defs>
    <polygon points="0,222 760,80 760,434 0,434" fill="url(#goldFill)"/>
  </svg>

  <div class="portrait" role="img" aria-label="Portrait photo of Dana Corwell in a dark blazer and yellow blouse"></div>

  <div class="brand-mark front-logo">
    <span class="brand-dot"></span>
    <span class="brand-name">Brightpath Holdings</span>
  </div>

  <div class="details">
    <h1 class="person-name">Dana Corwell, <span class="credentials">CPA, CMA</span></h1>
    <ul class="roles">
      <li>Entrepreneur &amp; Investor</li>
      <li>Business Ownership Transition Expert</li>
      <li>Multi-State Licensed Real Estate Broker</li>
    </ul>
    <ul class="contacts">
      <li>
        <svg viewBox="0 0 24 24" aria-hidden="true"><path d="M6.6 10.8a15.1 15.1 0 0 0 6.6 6.6l2.2-2.2a1 1 0 0 1 1-.25 11.4 11.4 0 0 0 3.6.57 1 1 0 0 1 1 1V20a1 1 0 0 1-1 1A17 17 0 0 1 3 4a1 1 0 0 1 1-1h3.5a1 1 0 0 1 1 1c0 1.25.2 2.45.57 3.57a1 1 0 0 1-.25 1z" fill="var(--ink)"/></svg>
        954-BRTPATH (278-7284)
      </li>
      <li>
        <svg viewBox="0 0 24 24" aria-hidden="true"><rect x="2" y="5" width="20" height="14" fill="var(--ink)"/><path d="M2 5l10 8 10-8" stroke="var(--gold-light)" stroke-width="1.6" fill="none"/></svg>
        Dana@BrightpathHoldings.com
      </li>
      <li>
        <svg viewBox="0 0 24 24" aria-hidden="true"><circle cx="12" cy="12" r="9.5" fill="none" stroke="var(--ink)" stroke-width="2"/><ellipse cx="12" cy="12" rx="4" ry="9.5" fill="none" stroke="var(--ink)" stroke-width="1.6"/><path d="M2.5 12h19M4 7h16M4 17h16" stroke="var(--ink)" stroke-width="1.4"/></svg>
        www.Brightpath.com
      </li>
    </ul>
  </div>
</section>

</body>
</html>
```